Brindle Oak Cellar & City of Alder Ridge; Public Forum: "Community in Action & Economic Deve...

To Whom it may concern; My name is Gordon Ellis Marsh and I am the owner of Brindle Oak Cellar LLC. I live in eastern Oregon in a town called Ontario. I'm originally from a smaller town 12 miles south of Ontario called Alder Ridge Oregon and that's where this project or the location of my business is going to be located along with moving my family. My Grandfather started a Beer & Winn Wholesaler in 1965 in Alder Ridge called Brindle Supply, my father was second generation owner and I had always planned on being 3rd. Well, with big business changing how things work with business consolidating to spread the cost of debt and KorMalt purchase of Dellacourt Frame, I wouldn't have been approved to buy(franchise agreement). So, bare with me, I tell you this because this information that you'll need to know for the project. My grandfather and Father built a legacy in Alder Ridge Oregon and were known for; Ethics and Morals, involvement in the community, fundraisers, donations, charity work, public service (volunteer firefighters), endowment scholarship fundraisers, etc....so my grandfather and dad were and are a big fish in a little pond but both are my hero's.

For the last 17 years I've been involved with the Cascade Patient Herb Registry CPHR. Its operated through; BFW; Bureau of Family Welfare @ CCA; Cascade Care Agency. I have seen many changes throughout the program. I have a Medical Marijuana Patient card, several Medical Marijuana Caregiver cards, grower cards but the grower cards have been replaced with a Grow Site Administrator card and I am a GSA. So my trade has been indoor cultivation and growing for patients who aren't able due to either health or the financial burdens that an indoor grow requires. Helping others (patients) find relief in whatever aliment they might be fighting has been very rewarding and I love the science behind growing.
In 2015 Oregon passed reactional Marijuana and it is ran by the CBRB; Cascade Beverage Review Board. Governor Falkner of Oregon gave local government (city council) the option of opting out of the program which has a 6 tier system with different licensing. Malheur County in which I lived opted out immediately along with Ontario and Alder Ridge Oregon. Well, Ontario Oregon lifted the ban about 1 year ago and it was a battle but people have slowly started to sway their opinion towards Cannabis. But, now Ontario Oregon is receiving all of the tax benefits that the CBRB program has to offer along with some city sales taxes on the product and Ontario is thriving. Malheur County and the cities within are the poorest in the state, so the tax benefits will go a long way.

PROJECT; I'm a family man.. my wife and I have 4 kids and have decided to move out of Ontario and to my home town in Alder Ridge (12 miles south of Ontario). I have been working with the community of Alder Ridge and the City of Alder Ridge (City Council, Police Department, Fire Department and Chamber of Commerce) in lifting the ban on reactional Marijuana in Alder Ridge Oregon. I am only asking for 2 out of the 6 licenses and will explain that along with the local politics and my business plan with some attachments. I have done my homework and leg work with this project but ran into an issue and this Is why I'm seeking outside help on the development of a power point. I finally reached my last step, in which was my presentation to the community and city council. I had put together a power point myself and used that for my presentation (I will send you this power point as well). .

I'm going to be having a Public Forum held In Alder Ridge Oregon so I can get the community to come out and get the right information and ask questions...I was going to see if you guys would design me a power point presentation....I do have one, but I really want a more professional touch...I can send you; business plan, city council power point and some other information....

Thanks,
Gordon Ellis Mars
Brindle Oak Cellar

Target Market(s)

Alder Ridge Oregon City Council Members and the Community/Citizens of Alder Ridge Oregon

Font styles to use
Sans Serif

Colors

Designer to choose only greyscale colors for use in the design.

Requirements
Must have
• bullet points; on key topics showing what our intent is and what isn't our intent
• heart and passion; getting Alder Ridge in which is directly on the border with Idaho who is illegal in both medical and recreational marijuana has been huge. Getting the band lifted the Governor Falkner gave city or counties the option to do has been a daunting task.
• Clarity with no chance of misunderstanding my company's intent; i can send you folks some articles and a power point that i put together for the city council as reference.
• market analysis section; so not only will we be talking about the 3% city sales tax on either my recreational production license or the wholesale license, but we will be my company is donating another 3% with our Neighbors Forward Giving Pool. Also, if we can't get a city sales tax on one of those licenses then my company pledges to up our neighbors forward giving pool another 3% to make that a 6% donation on monthly profits. finally, i would like to show the community of Alder Ridge in visual aids such as graphs,a basic market analysis on what the state of oregon has been bringing in with the tax benefits from recreational marijuana, the city of Huntington Oregon (close to Ontario and opened up their market a couple years before Ontario Oregon did) and finally Ontario Oregon (12 miles north from Alder Ridge Oregon) and what they have been bringing in with the tax benefits.
Nice to have
• company logo
• pictures of my family
• pictures of Alder Ridge Oregon
• some positive uplifting quotes on change, trust and family
Should not have
• no Pictures of Marijuana (out of sight out of mind)

```html
<!DOCTYPE html>
<html lang="en">
<head>
<meta charset="utf-8">
<title>Brindle Oak Cellar – Master Slides</title>
<link href="https://fonts.googleapis.com/css2?family=Montserrat:wght@300;400;500;600;700;800&family=Open+Sans:wght@400;600;700&display=swap" rel="stylesheet">
<style>
:root{
  --canvas:#000000;
  --slide:#3b3b3b;
  --slide-deep:#2c2c2c;
  --card:#404040;
  --gold:#fbc76a;
  --gold-deep:#e8ae4a;
  --white:#ffffff;
  --ink:#2e2e2e;
  --muted:#8a8a8a;
}
*{box-sizing:border-box;margin:0;padding:0}
html,body{width:1200px;height:2463px;overflow:hidden;background:var(--canvas)}
body{position:relative;font-family:"Open Sans",Arial,sans-serif;color:var(--white)}
.slide{position:absolute;width:545px;height:306px;background:var(--slide);overflow:hidden}
.col-l{left:34px}.col-r{left:621px}
.row1{top:37px}.row2{top:381px}.row3{top:724px}.row4{top:1067px}.row5{top:1410px}.row6{top:1754px}.row7{top:2097px}
.abs{position:absolute}
.photo{position:absolute}
.brand{font-family:"Montserrat",Arial,sans-serif;font-weight:300;color:var(--gold);text-transform:uppercase;letter-spacing:.06em;white-space:nowrap}
.brand-mark{position:absolute;border:2px solid var(--gold)}
.tagline{font-family:"Montserrat",Arial,sans-serif;font-weight:400;color:var(--gold);font-size:6.5px;letter-spacing:.08em;text-transform:uppercase;white-space:nowrap}
.hdr-bar{position:absolute;left:0;top:20px;width:9px;height:26px;background:var(--gold)}
.hdr{position:absolute;left:24px;top:22px;font-family:"Montserrat",Arial,sans-serif;font-size:17.5px;font-weight:700;color:var(--white);line-height:1.2;white-space:nowrap}
.hdr span{color:var(--gold);font-weight:500}
.corner-logo{position:absolute;left:483px;top:20px;width:50px;text-align:center}
.corner-logo i{display:block;width:13px;height:15px;margin:0 auto 2px;border:1.3px solid var(--gold)}
.corner-logo b{display:block;font-family:"Montserrat",Arial,sans-serif;font-weight:400;color:var(--gold);font-size:4.3px;letter-spacing:.04em}
.footline{position:absolute;left:0;right:0;top:300px;height:1.5px;background:var(--gold)}
.pg{position:absolute;right:2px;top:290px;width:15px;height:13px;background:var(--gold);color:var(--ink);font-family:"Montserrat",Arial,sans-serif;font-size:5.5px;font-weight:700;text-align:center;line-height:13px}
.icon-ring{position:absolute;border:2px solid var(--gold);border-radius:50%}
ul.list{list-style:none}
ul.list li{position:relative;padding-left:11px}
ul.list li::before{content:"";position:absolute;left:1px;top:.62em;width:3px;height:3px;border-radius:50%;background:currentColor}
ul.arrows{list-style:none}
ul.arrows li{position:relative;padding-left:13px}
ul.arrows li::before{content:"\27A2";position:absolute;left:0;top:0;font-size:.85em}
.hl{color:var(--gold);font-weight:700}
.quote-mark{position:absolute;font-family:"Montserrat",Arial,sans-serif;font-weight:800;line-height:1}
.pledge{position:absolute;top:181px;height:88px;background:var(--gold);border-radius:10px;overflow:hidden;box-shadow:0 3px 8px rgba(0,0,0,.4)}
.pledge-title{background:var(--white);height:19px;text-align:center;font-family:"Montserrat",Arial,sans-serif;font-size:8px;font-weight:600;color:var(--ink);line-height:19px}
.pledge p{text-align:center;font-size:7.5px;line-height:9.6px;color:var(--ink)}
.market-points li::before{content:"";display:inline-block;width:4px;height:4px;background:var(--white);margin-right:8px;vertical-align:middle}
.caption{position:absolute;top:2426px;left:0;width:1200px;text-align:center;font-family:"Montserrat",Arial,sans-serif;font-size:17px;font-weight:400;letter-spacing:.04em;color:var(--white)}
</style>
</head>
<body>

<section class="slide col-l row1 title-slide" style="background:var(--slide-deep)">
  <div class="abs" style="left:20px;top:51px;width:508px;height:205px;border:2px solid var(--gold-deep)"></div>
  <div class="abs" style="left:154px;top:0;width:236px;height:271px;background:var(--card);box-shadow:0 4px 14px rgba(0,0,0,.5)"></div>
  <div class="brand-mark" style="left:236px;top:90px;width:74px;height:84px"></div>
  <div class="brand abs" style="left:154px;width:236px;top:190px;text-align:center;font-size:19px;letter-spacing:.02em">Brindle Oak Cellar</div>
  <div class="tagline abs" style="left:154px;width:236px;top:219px;text-align:center;font-size:8px">"Rooted in Tomorrow"</div>
</section>

<section class="slide col-r row1 intro-slide">
  <div class="photo" role="img" aria-label="Family portrait of the owner, his wife and three children at home" style="inset:0;background:linear-gradient(160deg,#8a7a6e 0%,#5e4e45 45%,#3a302c 100%)"></div>
  <div class="brand-mark" style="left:56px;top:13px;width:30px;height:34px"></div>
  <div class="brand abs" style="left:16px;top:60px;font-size:9.5px;color:#f0e3cc">Brindle Oak Cellar</div>
  <div class="tagline abs" style="left:36px;top:73px;font-size:4.5px;color:#f0e3cc">Rooted in Tomorrow</div>
  <div class="abs" style="left:0;width:545px;top:240px;text-align:center;padding-left:40px;font-family:'Montserrat',Arial,sans-serif;font-weight:700;font-size:21px;color:var(--white);white-space:nowrap">Brindle O-C &amp; The City of Alder Ridge</div>
  <div class="abs" style="left:0;width:545px;top:270px;text-align:center;padding-left:40px;font-size:9.5px;color:var(--white);white-space:nowrap">"Community In Action, Control, Transparent and Economic Development"</div>
  <div class="abs" style="left:270px;top:285px;width:44px;height:2px;background:var(--gold)"></div>
</section>

<section class="slide col-l row2 agenda-slide" style="background:var(--white)">
  <div class="photo" role="img" aria-label="Landscape of a lake and cliffs at sunset" style="left:0;top:0;width:188px;height:136px;background:linear-gradient(180deg,#7f8ea0 0%,#c9b08a 38%,#3f6f8c 62%,#5b4a3c 100%)"></div>
  <div class="abs" style="left:0;top:136px;width:188px;height:170px;background:var(--slide)"></div>
  <div class="abs" style="left:88px;top:68px;width:155px;height:38px;background:var(--white);box-shadow:0 3px 10px rgba(0,0,0,.35);font-family:'Montserrat',Arial,sans-serif;font-weight:700;font-size:19px;color:var(--ink);text-align:center;line-height:38px;letter-spacing:.02em">AGENDA</div>
  <div class="brand-mark" style="left:72px;top:186px;width:42px;height:48px"></div>
  <div class="brand abs" style="left:0;width:188px;top:241px;text-align:center;font-size:12px;letter-spacing:.02em">Brindle Oak Cellar</div>
  <div class="tagline abs" style="left:0;width:188px;top:256px;text-align:center;font-size:4.8px">"Rooted in Tomorrow"</div>
  <div class="abs" style="left:542px;top:0;width:3px;height:306px;background:var(--gold)"></div>
  <ol class="abs agenda-list" style="left:280px;top:59px;list-style:none;font-family:'Montserrat',Arial,sans-serif;font-weight:500;font-size:9.3px;color:var(--ink);line-height:24.5px;white-space:nowrap">
    <li>01. COMPANY SUMMARY</li>
    <li>02. MISSION STATEMENT</li>
    <li>03. KNOW YOUR BUSINESS LICENSE TYPES</li>
    <li>04. TYPE OF LICENSSING</li>
    <li>05. GOALS</li>
    <li>06. MARKET REVIEW AND TAX BENEFITS</li>
    <li>07. OVERVIEW STATEMENT</li>
    <li>08. MY INTERNAL GRATITUDE AND DEEP</li>
    <li style="padding-left:19px">THOUGHTS W/ GORDON MARSH</li>
  </ol>
</section>

<section class="slide col-r row2 quote-slide">
  <div class="abs" style="left:18px;top:51px;width:509px;height:206px;border:1.5px solid var(--white)"></div>
  <div class="abs" style="left:0;top:105px;width:545px;height:96px;background:var(--gold)"></div>
  <div class="quote-mark" style="left:24px;top:98px;font-size:54px;color:var(--slide)">&ldquo;</div>
  <div class="abs" style="left:84px;top:113px;width:395px;font-family:'Montserrat',Arial,sans-serif;font-weight:700;font-size:22px;line-height:27.5px;color:var(--slide)"><span style="color:var(--white)">Ethics is</span> knowing the difference between what you have a right to do and what is right to do.</div>
  <div class="quote-mark" style="left:484px;top:160px;font-size:54px;color:var(--slide)">&rdquo;</div>
</section>

<section class="slide col-l row3 summary-slide">
  <div class="hdr-bar"></div>
  <div class="hdr">COMPANY <span>SUMMARY</span></div>
  <div class="corner-logo"><i></i><b>BRINDLE OAK CELLAR</b></div>
  <div class="quote-mark" style="left:22px;top:46px;font-size:48px;color:var(--muted)">&ldquo;</div>
  <p class="abs" style="left:24px;top:88px;width:496px;font-size:9.2px;line-height:16.4px;text-align:justify;color:var(--white)">Brindle oak cellar will be modeled after my father and grandfather business practices. One of our main goals will be to earn the community of Alder Ridge's trust through our actions. Community involvement, drug awareness, and becoming a member of the chamber would honor our company and being able to give back to a community that gave me a safe and amazing childhood.</p>
  <div class="quote-mark" style="left:488px;top:128px;font-size:48px;color:var(--muted)">&rdquo;</div>
  <div class="pledge" style="left:57px;width:129px">
    <div class="pledge-title">PLEDGE#1</div>
    <p style="padding:5px 10px 0">BOC cant stress this enough and remains committed to keeping cannabis 100% out of the hands of all youths.</p>
  </div>
  <div class="pledge" style="left:209px;width:272px">
    <div class="pledge-title">PLEDGE#2</div>
    <p style="padding:5px 18px 0">BOC has no interest or would we ever try to change ones believes or core values and is not interested in making this a moral or ethical issue. Marijuana is a drug and it needs to be controlled and we feel that taking control and holding others accountable is the best way to handle this situation.</p>
  </div>
  <div class="footline"></div><div class="pg">5</div>
</section>

<section class="slide col-r row3 mission-slide">
  <div class="hdr-bar"></div>
  <div class="hdr">MISSION <span>STATEMENT</span></div>
  <div class="corner-logo"><i></i><b>BRINDLE OAK CELLAR</b></div>
  <div class="icon-ring" style="left:233px;top:67px;width:59px;height:59px"></div>
  <svg class="abs" style="left:247px;top:81px" width="31" height="31" viewBox="0 0 24 24" fill="none" stroke="#fbc76a" stroke-width="1.8" stroke-linejoin="round" stroke-linecap="round"><path d="M14 4c3-1.5 5.5-1 6-.5s1 3-.5 6L13 16l-5-5z"/><path d="M9 9H5l-2 3 4 1"/><path d="M15 15v4l-3 2-1-4"/><path d="M6 16c-1.5 1-2 3-2 4 1 0 3-.5 4-2"/></svg>
  <div class="abs" style="left:20px;top:146px;width:3px;height:5px;background:var(--gold)"></div>
  <p class="abs" style="left:31px;top:143px;width:265px;font-size:8.6px;line-height:16.4px;text-align:justify;color:var(--white)">To create a name brand of the highest of quality, with an emphasis on medical applications that holds CONTROL and the strict regulations governed by the city of Alder Ridge and the CBRB. In doing this; we will bring economic development, growth, family waged jobs and several new tax benefits that can greatly increase the prosperity of Alder Ridge.</p>
  <div class="abs" role="img" aria-label="Company registration seal" style="left:322px;top:66px;width:203px;height:203px;border-radius:50%;background:radial-gradient(circle at 40% 35%,#f3d48a 0%,#d9a94c 55%,#a8772a 100%);box-shadow:0 4px 12px rgba(0,0,0,.45)"></div>
  <div class="footline"></div><div class="pg">6</div>
</section>

<section class="slide col-l row4 licenses-slide">
  <div class="abs" style="left:0;top:0;width:380px;height:306px;background:var(--white)"></div>
  <div class="abs" style="left:380px;top:0;width:4px;height:306px;background:var(--gold)"></div>
  <div class="hdr-bar"></div>
  <div class="hdr" style="color:var(--ink);font-size:16.5px">KNOW YOUR <span style="color:var(--gold-deep);font-weight:700;padding-left:3px;font-size:15.5px">BUSINESS LICENSE TYPES</span></div>
  <div class="corner-logo"><i></i><b>BRINDLE OAK CELLAR</b></div>
  <div class="abs" style="left:48px;top:71px;width:320px;color:var(--ink);font-size:6.3px;line-height:10.4px">
    <div style="font-weight:700;font-size:6.8px;margin-bottom:5px">CBRB Licenses</div>
    <ul class="list">
      <li><b>Producer:</b><br>Ability to plant, cultivate, grow, harvest, and dry marijuana.</li>
      <li><b>Processor:</b><br>Ability to process, compound, or convert marijuana into cannabinoid products, concentrates, and/or extracts.</li>
      <li><b>Wholesale:</b><br>Can purchase quantities of marijuana from other licensed facilities and sell the products to licensed retailers, processors, producers, other wholesalers, or research certificate holders.</li>
      <li><b>Laboratory:</b><br>Accredited by CALAP and responsible for testing marijuana items for pesticides, solvents or residual solvents, tetrahydrocannabinol and cannabidiol concentration, and for microbiological or other contaminants.</li>
      <li><b>Retail:</b><br>Can sell or deliver marijuana items directly to consumers.</li>
      <li><b>Research Certificate:</b><br>Ability to research marijuana for the purpose of benefiting the state's cannabis industry, medical research, or public health and safety.</li>
    </ul>
  </div>
  <div class="abs" style="left:393px;top:134px;width:145px;height:40px;border:1.5px solid var(--gold);font-family:'Montserrat',Arial,sans-serif;font-weight:700;font-size:19px;letter-spacing:.1em;color:var(--white);text-align:center;line-height:37px">SECTION 1</div>
  <div class="footline"></div><div class="pg">7</div>
</section>

<section class="slide col-r row4 licensing-slide">
  <div class="hdr-bar"></div>
  <div class="hdr">TYPE OF <span>LICENSSING</span></div>
  <div class="corner-logo"><i></i><b>BRINDLE OAK CELLAR</b></div>
  <div class="abs" style="left:25px;top:73px;width:204px;height:205px;background:var(--white);border-radius:12px;box-shadow:0 3px 10px rgba(0,0,0,.45);text-align:center;color:var(--ink)">
    <div style="margin-top:9px;font-family:'Montserrat',Arial,sans-serif;font-weight:700;font-size:14.5px;letter-spacing:.1em">PRODUCTION</div>
    <svg style="display:block;margin:8px auto 0" width="42" height="42" viewBox="0 0 42 42" fill="none" stroke="#2e2e2e" stroke-width="1.5"><circle cx="21" cy="21" r="19.5"/><circle cx="17" cy="19" r="7" stroke-dasharray="2.5 1.5"/><circle cx="17" cy="19" r="3"/><circle cx="27" cy="26" r="4.5" stroke-dasharray="2 1.3"/><circle cx="27" cy="26" r="1.8"/></svg>
    <div style="margin-top:10px;font-size:9px;line-height:16.3px">Strictly indoor tier 1<br>Zoned for out of sight out of mind policy<br>No advertising<br>No traffic<br>Contain smell<br>Strong security</div>
  </div>
  <div class="abs" style="left:255px;top:73px;width:290px;height:205px;background:var(--gold);color:var(--ink)">
    <div style="margin-top:9px;text-align:center;padding-right:50px;font-family:'Montserrat',Arial,sans-serif;font-weight:700;font-size:14.5px;letter-spacing:.1em">WHOLSALE</div>
    <svg style="display:block;margin:8px 0 0 93px" width="42" height="42" viewBox="0 0 42 42" fill="none" stroke="#2e2e2e" stroke-width="1.5"><circle cx="21" cy="21" r="19.5"/><circle cx="21" cy="21" r="11"/><ellipse cx="21" cy="21" rx="5" ry="11"/><path d="M10 21h22M12 15h18M12 27h18"/></svg>
    <ul class="arrows" style="margin:10px 0 0 20px;width:265px;font-size:7.3px;line-height:14.1px">
      <li>Ship, test and wholesale product out of the area</li>
      <li>Pledges to not create problems for the city of Alder Ridge; no extra traffic of any kind</li>
      <li>No advertising</li>
      <li>Never glorifying to our youth</li>
      <li>Wholesale out of the area to guarantee product gets turned into processing and medical applications</li>
      <li>In support of abolishment of the black-market</li>
    </ul>
  </div>
  <div class="footline"></div><div class="pg">8</div>
</section>

<section class="slide col-l row5 divider-slide">
  <div class="photo" role="img" aria-label="Family portrait of the owner, his wife and three children, darkened" style="inset:0;background:linear-gradient(150deg,#4a4340 0%,#3a3433 50%,#2f2b2a 100%)"></div>
  <div class="brand-mark" style="left:63px;top:22px;width:40px;height:45px"></div>
  <div class="brand abs" style="left:25px;top:73px;font-size:12px;letter-spacing:.02em">Brindle Oak Cellar</div>
  <div class="tagline abs" style="left:46px;top:88px;font-size:4.8px">"Rooted in Tomorrow"</div>
  <div class="abs" style="right:22px;top:203px;text-align:right;font-family:'Montserrat',Arial,sans-serif;font-weight:700;font-size:25px;line-height:29px;color:var(--white)">BUSINESS<br>ASSUMPTIONS &amp; GOALS</div>
  <div class="abs" style="right:22px;top:265px;font-size:8.4px;color:var(--white);white-space:nowrap">Opportunity, creating growth and prosperity to the community of Alder Ridge</div>
  <div class="abs" style="left:536px;top:203px;width:9px;height:60px;background:var(--gold)"></div>
</section>

<section class="slide col-r row5 goals-slide">
  <div class="hdr-bar"></div>
  <div class="hdr">GOALS &amp; MAIN BULLET <span>POINTS</span></div>
  <div class="corner-logo"><i></i><b>BRINDLE OAK CELLAR</b></div>
  <ul class="list abs" style="left:24px;top:57px;width:495px;font-size:8.4px;line-height:12.3px;color:var(--white)">
    <li>Family Wage Jobs</li>
    <li>Intracellular part of the community of Alder Ridge (like my grandfather and father before me).</li>
    <li>Give back to the community; participating and organizing awareness and fundraisers for drug abuse and other areas in which the community could use extra funding,</li>
    <li>Create additional revenue; city tax &amp; neighbors forward giving pool</li>
    <li><span class="hl">STRICTLY INDOOR PRODUCTION FACILTY;</span> with an out of sight out of mind policy, <span class="hl">NO ADVERTSING, NO GLORFYING</span></li>
    <li>full compliance with CBRB and City of Alder Ridge regulatory agencies, tackling within a pending status any and all concerns pending walkthrough with CBRB; ODOR CONCERNS, SECURITY CONCERNS, ETC.</li>
    <li><span class="hl">NOT ASKING FOR A RETAIL OPERATION;</span> traffic and flux of people is not something we are seeking but trying to avoid</li>
    <li><span class="hl">PRODUCT WILL BE TAKEN OUT OF THE AREA (ACROSS THE STATE),</span> This alleviates and helps BOC guarantee that our product will not be getting into the hands of our children.</li>
    <li>Allocation of funds for a swimming pool</li>
    <li>Work and build healthy working relationships with the local chamber, city police, fire department and city council</li>
    <li>100% committed in fundraisers in all aspects; drug awareness, Alder Ridge downtown Revitalization, endowment scholarships, etc.</li>
  </ul>
  <div class="footline"></div><div class="pg">10</div>
</section>

<section class="slide col-l row6 market-slide">
  <div class="hdr-bar"></div>
  <div class="hdr">MARKET REVIEW <span>AND TAX BENIFITS</span></div>
  <div class="corner-logo"><i></i><b>BRINDLE OAK CELLAR</b></div>
  <div class="abs" style="left:0;top:68px;width:200px;height:238px;background:var(--gold)"></div>
  <p class="abs" style="left:24px;top:78px;width:160px;font-family:'Montserrat',Arial,sans-serif;font-weight:600;font-size:11.3px;line-height:20.4px;color:var(--white)"><span style="opacity:.8">At the request of the council;</span><br>( I will have a market analysis done on Alder Ridge with factual numbers and data of tax benefits that a recreational indoor production facility could create for the community ).</p>
  <ul class="abs market-points" style="left:224px;top:102px;list-style:none;font-family:'Montserrat',Arial,sans-serif;font-weight:500;font-size:11px;color:var(--white);line-height:41px;white-space:nowrap">
    <li>3% city sales tax</li>
    <li>Conservative base point around $100,000 a month</li>
    <li>Community action fund donating another 3%</li>
    <li>Potential grand total of $6,000 a month to Alder Ridge</li>
  </ul>
  <div class="footline"></div><div class="pg">11</div>
</section>

<section class="slide col-r row6 overview-slide">
  <div class="hdr-bar"></div>
  <div class="hdr">OVERVIEW <span>STATEMENT</span></div>
  <div class="corner-logo"><i></i><b>BRINDLE OAK CELLAR</b></div>
  <svg class="abs" style="left:233px;top:66px" width="62" height="62" viewBox="0 0 62 62" fill="none" stroke="#fbc76a" stroke-width="2"><circle cx="31" cy="31" r="29.5"/><circle cx="31" cy="31" r="18"/><circle cx="31" cy="31" r="11"/><circle cx="31" cy="31" r="4"/><path d="M31 31l13-13M40 15l4 3 3-3"/></svg>
  <ul class="arrows abs" style="left:28px;top:145px;width:500px;font-size:8.6px;line-height:16.4px;color:var(--white);text-align:justify">
    <li>Doing this on a professional manner while following all the state guidelines in which the Cascade Beverage Review Board has set forth. Along with the city of Alder Ridge</li>
    <li>Brindle oak cellar is Not asking for a retail license, as we feel this would an abrupt change to Alder Ridge with to much change to fast with increased traffic and a abundance of people. Pros and cons can be debated and discussed. It is of my opinion that some caution and restrain can still be and should be practiced when introducing the community to these new waters.</li>
    <li>Willing to form a Pac committee to help eliminate the black market and create a positive impact on the community while never advertising or glorifying to our youth.</li>
  </ul>
  <div class="footline"></div><div class="pg">12</div>
</section>

<section class="slide col-l row7 gratitude-slide">
  <div class="hdr-bar"></div>
  <div class="hdr" style="top:22px;line-height:20px">MY INTERNAL GRATITUDE AND DEEP<br>THOUGHTS W/ <span>GORDON MARSH</span></div>
  <div class="corner-logo"><i></i><b>BRINDLE OAK CELLAR</b></div>
  <p class="abs" style="left:31px;top:89px;width:212px;font-size:10.3px;line-height:18.5px;text-align:justify;color:var(--white)">I know what the community and the council have had to endear in the past with the out of state cards, unwanted traffic, pressure on community/council along with the black-market and all the risks that alone brings to our youths. So, thank you for not grouping me with those individuals and allowing me to give this presentation in which will be taking a very different approach.</p>
  <div class="abs" style="left:334px;top:79px;width:133px;height:198px;background:var(--gold)"></div>
  <div class="photo" role="img" aria-label="Portrait of a baby in a holiday outfit" style="left:347px;top:91px;width:136px;height:201px;background:linear-gradient(160deg,#d9d2cc 0%,#9c8f8a 45%,#7c3a36 100%);box-shadow:0 4px 10px rgba(0,0,0,.5)"></div>
  <div class="footline"></div><div class="pg">13</div>
</section>

<section class="slide col-r row7 closing-slide">
  <div class="photo" role="img" aria-label="Family walking together across a snowy field at sunset" style="inset:0;background:linear-gradient(180deg,#e7bf84 0%,#c99a66 35%,#8b7a72 65%,#bfc2cc 100%)"></div>
  <div class="brand-mark" style="left:64px;top:24px;width:38px;height:44px"></div>
  <div class="brand abs" style="left:22px;top:75px;font-size:11.5px;letter-spacing:.02em">Brindle Oak Cellar</div>
  <div class="tagline abs" style="left:42px;top:89px;font-size:4.6px">Rooted in Tomorrow</div>
  <p class="abs" style="left:0;width:545px;top:240px;text-align:center;font-family:'Montserrat',Arial,sans-serif;font-weight:700;font-size:13px;line-height:16.5px;color:var(--white)">Thank you for giving me your time today, and letting me present the<br>future of Alder Ridge to you my fellow community, and council members.</p>
</section>

<div class="caption">MASTER SLIDES PRESENTATION</div>

</body>
</html>
```